New Graphic Design Project*

We would like to design a 12ft x 6 ft wallpaper for a room where deprived teen children will study at a charity. Our idea is to create a motivational wallpaper with "hands and heart" "The power is in your hands" artwork in the center (PSD attached) and with our superhero incorporated in the design. Maybe sky blue and clouds white will be a good background but you can decide best. The other walls are painted darker blue.
We are thinking maybe different inspiring words scattered around would be successful so kids can look at it in a spur- to feel motivated and also protected by the superhero.
I know that true designers will get the idea.

Files here:
https://www.filvarobox.com/sh/3kq7tpwmzxhd2b4/BBRTkyuHbzqnXX11LmvdPwQcF?dl=0

Target Market(s)

charity/teen children

```html
<!DOCTYPE html>
<html lang="en">
<head>
<meta charset="utf-8">
<title>Motivational Wallpaper Panels</title>
<link rel="stylesheet" href="https://fonts.googleapis.com/css2?family=Bungee&family=Oswald:wght@700&family=Lilita+One&display=swap">
<style>
  :root {
    --navy: #061745;
    --frame: #ffffff;
    --sky: #1763dc;
    --sun-yellow: #ffd400;
    --sun-orange: #ffb000;
    --white: #ffffff;
    --red: #d8241c;
    --deep-red: #a8140e;
    --purple: #5b3aa8;
    --blue: #1c4fb8;
    --orange: #ff8a00;
    --gold: #ffe14a;
  }
  * { margin: 0; padding: 0; box-sizing: border-box; }
  html, body { width: 1200px; height: 649px; overflow: hidden; }
  body { background: var(--navy); position: relative; }

  .panel {
    position: absolute;
    top: 53px;
    width: 279px;
    height: 538px;
    background: var(--frame);
    padding: 9.5px 9px 8.5px 9.5px;
    box-shadow: 6px 8px 14px rgba(0, 0, 0, 0.35);
  }
  .panel--hero { left: 264px; }
  .panel--words { left: 638px; padding: 9.5px 10px 8.5px 8.5px; }

  .panel__art {
    position: relative;
    width: 100%;
    height: 100%;
    overflow: hidden;
  }

  /* Hero panel */
  .hero-art { background: var(--sky); }
  .slogan {
    position: absolute;
    left: 0; right: 0;
    top: 22px;
    text-align: center;
    font-family: "Bungee", sans-serif;
    font-weight: 400;
    color: var(--white);
    line-height: 1;
  }
  .slogan span { display: block; }
  .slogan__big { font-size: 44px; letter-spacing: 14px; padding-left: 14px; }
  .slogan__mid { font-size: 25px; letter-spacing: 7px; padding-left: 7px; margin-top: 0; }
  .slogan__small { font-size: 18px; letter-spacing: 1.5px; padding-left: 1.5px; margin-top: 0; }
  .slogan__hands { font-size: 26px; letter-spacing: 7.5px; padding-left: 7.5px; margin-top: 0; }

  .hero-figure {
    position: absolute;
    left: 0; top: 140px;
    width: 260px; height: 300px;
    background: radial-gradient(ellipse at 50% 45%, rgba(92, 84, 176, 0.9) 0%, rgba(92, 84, 176, 0.7) 35%, rgba(240, 180, 40, 0.45) 55%, rgba(23, 99, 220, 0) 72%);
  }

  .charity-mark {
    position: absolute;
    left: 0; right: 0;
    top: 450px;
    display: flex;
    align-items: center;
    justify-content: center;
    gap: 6px;
    font-family: "Bungee", sans-serif;
    font-size: 11px;
    color: var(--white);
  }
  .charity-mark__dot {
    width: 12px; height: 12px;
    border-radius: 50%;
    background: var(--white);
  }

  /* Words panel */
  .words-art {
    background: radial-gradient(ellipse at 50% 45%, var(--sun-yellow) 0%, #ffc800 60%, var(--sun-orange) 100%);
  }
  .word {
    position: absolute;
    left: 0; right: 0;
    text-align: center;
    line-height: 1;
    white-space: nowrap;
  }
  .word--strong {
    top: 78px;
    font-family: "Oswald", sans-serif;
    font-size: 46px;
    letter-spacing: 0.5px;
    color: var(--white);
    text-shadow: 2px 2px 0 var(--red), 3px 3px 0 var(--blue), 4px 4px 0 var(--blue);
  }
  .word--dream {
    top: 146px;
    font-family: "Lilita One", sans-serif;
    font-size: 58px;
    color: var(--orange);
    -webkit-text-stroke: 1.5px var(--purple);
    text-shadow: 0 3px 0 var(--purple), 0 5px 0 var(--purple), 0 9px 8px rgba(0, 0, 0, 0.35);
  }
  .word--imagine {
    top: 232px;
    font-family: "Lilita One", sans-serif;
    font-size: 54px;
    color: var(--orange);
    -webkit-text-stroke: 1.5px var(--red);
    text-shadow: 0 3px 0 var(--purple), 0 5px 0 var(--purple), 0 9px 8px rgba(0, 0, 0, 0.3);
  }
  .word--believe {
    top: 315px;
    font-family: "Lilita One", sans-serif;
    font-size: 50px;
    color: var(--gold);
    text-shadow: 0 2px 0 var(--orange), 0 4px 0 var(--blue), 0 6px 0 var(--blue), 0 10px 8px rgba(0, 0, 0, 0.3);
    transform: skewX(-6deg);
  }
  .word--achieve {
    top: 394px;
    font-family: "Lilita One", sans-serif;
    font-size: 52px;
    color: var(--gold);
    text-shadow: 1px 2px 0 var(--red), 2px 4px 0 var(--red), 3px 6px 0 var(--deep-red), 4px 12px 10px rgba(0, 0, 0, 0.35);
    transform: rotate(-2deg) skewX(-4deg);
  }
</style>
</head>
<body>
  <section class="panel panel--hero">
    <div class="panel__art hero-art">
      <h1 class="slogan">
        <span class="slogan__big">THE</span>
        <span class="slogan__mid">POWER</span>
        <span class="slogan__small">IS IN YOUR</span>
        <span class="slogan__hands">HANDS</span>
      </h1>
      <div class="hero-figure" role="img" aria-label="Illustrated superhero in purple and yellow suit leaping upward against the sky with soft clouds"></div>
      <div class="charity-mark">
        <span class="charity-mark__dot"></span>
        <span>Brightwing Trust</span>
      </div>
    </div>
  </section>

  <section class="panel panel--words">
    <div class="panel__art words-art" role="img" aria-label="Bright yellow comic burst background">
      <p class="word word--strong">BE STRONG</p>
      <p class="word word--dream">DREAM</p>
      <p class="word word--imagine">IMAGINE</p>
      <p class="word word--believe">BELIEVE</p>
      <p class="word word--achieve">ACHIEVE</p>
    </div>
  </section>
</body>
</html>
```